KLV Messaging - veteran and exclusive boutique copywriting agency

PROJECT NEEDS:
1. Website design - full homepage design and inner page top banner design
2. Logo design
* Please see attached Briefs (Word Docs) for descriptions of what is needed for 1 and 2 above.
ABOUT THE CLIENT:
KLV Messaging is a veteran and exclusive boutique copywriting agency run by Marcus Holloway. Marcus is an award-winning published novelist and an accomplished executive ghostwriter with articles regularly published prominent technology publications like Brisk, ByteHarbor, FoundryPulse, and more. For nearly three decades, Marcus has focused solely on the technology sector - serving clients in Israel, Europe and the US.

Target Market(s)

hi-tech companies run by serious, confident professionals.

Industry/Entity Type

Business

Number of Pages Required

2 page

Font styles to use
Sans Serif
Other font styles liked:
• font should be modern

Colors
0054AA
0677BA
7BADD7
CADEEF
E8F1F8
F0912C
F2A743
F7CA91
FBE8D2
FDF5EE

Requirements
Must have
• psd files for logo, homepage design, and inner page top banner design
Nice to have
• Please see attached Website and Logo Design Briefs (Word Docs)
Should not have

```html
<!DOCTYPE html>
<html lang="en">
<head>
<meta charset="utf-8">
<title>KLV Messaging — Your Voice, My Words.</title>
<link href="https://fonts.googleapis.com/css2?family=Montserrat:wght@400;500;600;700;800&family=Arimo:wght@400;700&display=swap" rel="stylesheet">
<style>
:root{
  --navy:#0b2447;
  --navy-deep:#071a35;
  --navy-header:#08203f;
  --ink:#0f2a4f;
  --orange:#f7931e;
  --page-light:#e9eef9;
  --card:#f6f8fd;
  --white:#ffffff;
  --logo-grey:#3a3a3a;
}
*{box-sizing:border-box;margin:0;padding:0}
html,body{width:1200px;height:2766px;overflow:hidden}
body{position:relative;background:var(--navy);font-family:"Arimo",Arial,sans-serif;color:var(--ink)}
.abs{position:absolute}

/* brand: name in one colour and weight, one plain circle beside */
.brand{font-family:"Montserrat",Arial,sans-serif;color:var(--white);font-size:20px;font-weight:600;display:flex;align-items:center;gap:9px;white-space:nowrap}
.brand-dot{width:11px;height:11px;border-radius:50%;background:var(--orange);display:block}

/* header */
.site-header{left:0;top:0;width:1200px;height:73px;background:var(--navy-header)}
.site-header .brand{left:161px;top:24px}
.nav{left:515px;top:26px;display:flex;gap:23px;font-family:"Montserrat",Arial,sans-serif;font-size:15px;font-weight:600;color:var(--white)}
.nav .active{color:var(--orange);text-decoration:underline;text-underline-offset:4px}
.nav-contact{left:918px;top:20px;width:92px;height:30px;border:2px solid var(--white);border-radius:2px;color:var(--white);font-family:"Montserrat",Arial,sans-serif;font-weight:700;font-size:15px;display:flex;align-items:center;justify-content:center}

/* hero */
.hero{left:0;top:73px;width:1200px;height:532px;background:radial-gradient(ellipse at 75% 40%,#0f3462 0%,#0b2447 55%,#091d3b 100%)}
.hero-title{left:218px;top:195px;font-family:"Montserrat",Arial,sans-serif;font-weight:800;font-size:52px;line-height:54px;color:var(--white);letter-spacing:1px}
.hero-lead{left:218px;top:311px;width:360px;font-size:19px;line-height:28px;color:var(--white)}
.btn-orange{background:var(--orange);color:var(--white);font-family:"Montserrat",Arial,sans-serif;font-weight:700;display:flex;align-items:center;justify-content:center;border-radius:2px}
.hero-book{left:218px;top:414px;width:122px;height:32px;font-size:17px}
.hero-ring{left:671px;top:143px}
.hero-portrait{left:732px;top:84px;width:300px;height:521px;border-radius:130px 130px 0 0;background:linear-gradient(180deg,#c8a690 0%,#8fb0d6 30%,#6f95c6 70%,#3e4a5a 100%)}

/* client strip */
.clients{left:0;top:605px;width:1200px;height:138px;background:var(--white)}
.client{top:657px;font-family:"Montserrat",Arial,sans-serif;font-weight:600;font-size:28px;color:var(--logo-grey);display:flex;align-items:center;gap:8px}
.client .dot{width:12px;height:12px;border-radius:50%;background:#111}

/* services */
.light-band{left:0;top:743px;width:1200px;height:1363px;background:var(--page-light)}
.eyebrow{font-family:"Montserrat",Arial,sans-serif;font-weight:500;color:var(--orange);font-size:24px}
.section-title{font-weight:700;color:var(--ink);font-size:25px;line-height:28px}
.what-eyebrow{left:0;width:1200px;top:778px;text-align:center}
.what-title{left:0;width:1200px;top:815px;text-align:center;line-height:31px}
.card{top:917px;width:266px;height:427px;background:var(--card);border-radius:6px;box-shadow:0 2px 8px rgba(15,42,79,.12);overflow:hidden}
.card-photo{width:266px;height:298px}
.card-name{position:absolute;left:11px;top:312px;font-family:"Montserrat",Arial,sans-serif;font-weight:700;font-size:16px;color:var(--ink)}
.card-text{position:absolute;left:11px;top:338px;width:220px;font-size:8.5px;line-height:12px;color:#333;text-align:justify}
.card-rule{position:absolute;left:11px;top:388px;width:244px;height:1px;background:#9aa3b2}
.card-more{position:absolute;left:11px;top:401px;font-family:"Montserrat",Arial,sans-serif;font-size:14px;color:#555;font-weight:500}
.dots{left:581px;top:1377px;display:flex;gap:6px}
.dots i{width:8px;height:8px;border-radius:50%;background:#1f4c8f;display:block}

/* why */
.why-photo{left:191px;top:1436px;width:304px;height:453px;border-radius:14px;background:linear-gradient(160deg,#3a3634 0%,#6b5242 45%,#8a5a35 80%,#5a3d28 100%)}
.badge{left:431px;top:1805px;width:136px;height:67px;border-radius:4px;background:var(--orange);color:var(--white);text-align:center}
.badge strong{display:block;font-family:"Montserrat",Arial,sans-serif;font-size:28px;line-height:30px;margin-top:5px}
.badge span{font-size:15px}
.why-eyebrow{left:600px;top:1449px}
.why-title{left:600px;top:1485px;width:410px}
.why-text{left:600px;top:1578px;width:370px;font-size:15.5px;line-height:21.5px;color:#2a3b5a}
.checks{left:600px;top:1686px;list-style:none}
.checks li{display:flex;align-items:center;gap:7px;font-size:16.5px;color:#2a3b5a;height:38px}
.btn-navy{left:600px;top:1810px;width:108px;height:29px;background:var(--navy);color:var(--white);font-family:"Montserrat",Arial,sans-serif;font-weight:700;font-size:16px;display:flex;align-items:center;justify-content:center;border-radius:2px}

/* testimonials */
.quote-panel{left:127px;top:1977px;width:946px;height:384px;background:var(--navy-deep);border-radius:8px}
.testi-eyebrow{left:191px;top:2091px}
.testi-title{left:191px;top:2130px;color:var(--white);font-size:27px}
.quote{left:600px;top:2075px;width:409px;font-family:"Montserrat",Arial,sans-serif;font-size:17.5px;line-height:23.6px;color:var(--white);text-align:justify;font-weight:400;letter-spacing:.4px}
.quote-name{left:600px;top:2231px;font-family:"Montserrat",Arial,sans-serif;font-weight:700;font-size:11.5px;color:var(--white)}
.quote-role{left:600px;top:2248px;font-family:"Montserrat",Arial,sans-serif;font-size:11.5px;color:var(--white)}
.quote-arrows{left:923px;top:2240px}

/* footer */
.footer-title{left:191px;top:2428px;font-family:"Montserrat",Arial,sans-serif;font-weight:800;font-size:29px;line-height:32px;color:var(--white)}
.site-footer-brand{left:191px;top:2524px}
.subscribe-input{left:191px;top:2586px;width:228px;height:43px;background:var(--white);font-family:"Montserrat",Arial,sans-serif;font-size:13px;color:#666;padding-left:15px;display:flex;align-items:center}
.subscribe-btn{left:419px;top:2586px;width:119px;height:43px;font-size:17px;font-weight:600;color:var(--navy);border-radius:0}
.foot-col h3{font-family:"Montserrat",Arial,sans-serif;font-weight:700;font-size:21px;color:var(--white);margin-bottom:12px}
.foot-col p{font-family:"Montserrat",Arial,sans-serif;font-size:14.5px;color:var(--white);line-height:16px;margin-bottom:11px}
.col-company{left:650px;top:2431px}
.col-contact{left:858px;top:2431px}
.foot-rule{left:191px;top:2676px;width:818px;height:1px;background:#4f6384}
.copyright{left:0;width:1200px;top:2702px;text-align:center;font-family:"Montserrat",Arial,sans-serif;font-weight:600;font-size:12.5px;color:var(--white)}
</style>
</head>
<body>

<header class="abs site-header">
  <div class="abs brand"><i class="brand-dot"></i>KLV Messaging</div>
  <nav class="abs nav">
    <span class="active">Home</span><span>About</span><span>Services</span><span>Industries</span><span>Clients</span>
  </nav>
  <div class="abs nav-contact">Contact</div>
</header>

<section class="abs hero"></section>
<svg class="abs hero-ring" width="392" height="392" viewBox="0 0 392 392" aria-hidden="true">
  <circle cx="196" cy="196" r="194" fill="#0a2142" opacity=".55"/>
  <circle cx="196" cy="196" r="194" fill="none" stroke="#f7931e" stroke-width="2"/>
</svg>
<div class="abs hero-portrait" role="img" aria-label="Portrait of Marcus Holloway standing, light blue shirt, dark trousers"></div>
<h1 class="abs hero-title">Your Voice, My<br>Words.</h1>
<p class="abs hero-lead">Copywriting and executive ghostwriting that speaks for your <b>vision</b> and your technology.</p>
<div class="abs btn-orange hero-book">Book Now</div>

<section class="abs clients" aria-label="Clients"></section>
<div class="abs client" style="left:100px">ORVANA</div>
<div class="abs client" style="left:318px;font-weight:400;color:#666">Kestrelo</div>
<div class="abs client" style="left:537px;color:#111">Lumora</div>
<div class="abs client" style="left:736px;font-size:20px;color:#111"><i class="dot"></i>QUILLSTONE</div>
<div class="abs client" style="left:922px;font-size:22px;font-weight:400;color:#8a8a8a">HALVERN MEDICAL</div>

<section class="abs light-band"></section>
<p class="abs eyebrow what-eyebrow">What I Do</p>
<h2 class="abs section-title what-title">Revolutionizing the tech industry<br>one article at a time</h2>

<article class="abs card" style="left:167px">
  <div class="card-photo" role="img" aria-label="Hands typing on a laptop keyboard" style="background:linear-gradient(160deg,#e8e4de 0%,#b99a80 45%,#6e6660 100%)"></div>
  <h3 class="card-name">Messaging</h3>
  <p class="card-text">The Value of a Fresh Perspective. Could you be reaching farther? Clearly-defined, accurately-targeted messaging is crucial.</p>
  <i class="card-rule"></i>
  <span class="card-more">Read More</span>
</article>
<article class="abs card" style="left:468px">
  <div class="card-photo" role="img" aria-label="Two people gesturing in a meeting" style="background:linear-gradient(150deg,#2a2a2e 0%,#4c4a4d 40%,#b58a78 70%,#5b5052 100%)"></div>
  <h3 class="card-name" style="top:317px">Collateral</h3>
  <p class="card-text" style="top:343px">Concise. Effective. Creative. Marketing collateral that effectively communicates who you are and what you want to say.</p>
  <i class="card-rule"></i>
  <span class="card-more">Read More</span>
</article>
<article class="abs card" style="left:766px">
  <div class="card-photo" role="img" aria-label="Hand writing notes beside a laptop" style="background:linear-gradient(160deg,#8fb3ad 0%,#c7d7d2 45%,#e7ece8 70%,#4d5a5e 100%)"></div>
  <h3 class="card-name" style="top:317px">Content Marketing</h3>
  <p class="card-text" style="top:343px">Giving Voice to Your Vision. Articles, blog content, white papers, e-books. Your ideas and expertise, our words.</p>
  <i class="card-rule"></i>
  <span class="card-more">Read More</span>
</article>
<div class="abs dots"><i></i><i></i><i></i></div>

<div class="abs why-photo" role="img" aria-label="Portrait of Marcus Holloway in a brown jacket"></div>
<div class="abs badge"><strong>50+</strong><span>Satisfied Clients</span></div>
<p class="abs eyebrow why-eyebrow">Why Choose me</p>
<h2 class="abs section-title why-title">I've created collateral and content for tens of companies across a wide range of industries.</h2>
<p class="abs why-text">At KLV Messaging, we believe that with the luxury of being a small company comes the obligation to treat the client like a friend, showing flexibility, helpfulness, and willingness to go the</p>
<ul class="abs checks">
  <li><svg width="20" height="20" viewBox="0 0 20 20" aria-hidden="true"><circle cx="10" cy="10" r="10" fill="#0b2447"/><path d="M5.5 10.3l3 3 6-6.3" fill="none" stroke="#fff" stroke-width="2.2"/></svg>100% Satisfaction</li>
  <li><svg width="20" height="20" viewBox="0 0 20 20" aria-hidden="true"><circle cx="10" cy="10" r="10" fill="#0b2447"/><path d="M5.5 10.3l3 3 6-6.3" fill="none" stroke="#fff" stroke-width="2.2"/></svg>Professional &amp; effective content</li>
  <li><svg width="20" height="20" viewBox="0 0 20 20" aria-hidden="true"><circle cx="10" cy="10" r="10" fill="#0b2447"/><path d="M5.5 10.3l3 3 6-6.3" fill="none" stroke="#fff" stroke-width="2.2"/></svg>Unique and tailored services</li>
</ul>
<div class="abs btn-navy">Read More</div>

<section class="abs quote-panel" aria-label="Testimonials"></section>
<p class="abs eyebrow testi-eyebrow">Testimonials</p>
<h2 class="abs section-title testi-title">What they're saying</h2>
<blockquote class="abs quote">"Marcus has rich experience in the security arena, and a unique ability to get up to speed quickly on new material. He has produced excellent collateral for us over the past three years, and I highly recommend him to other security companies</blockquote>
<p class="abs quote-name">Dana Whitcombe</p>
<p class="abs quote-role">CMO, Cobalt Ridge...</p>
<svg class="abs quote-arrows" width="86" height="14" viewBox="0 0 86 14" aria-hidden="true">
  <path d="M34 7H2M8 2L2 7l6 5" fill="none" stroke="#fff" stroke-width="2"/>
  <path d="M52 7h32M78 2l6 5-6 5" fill="none" stroke="#fff" stroke-width="2"/>
</svg>

<h2 class="abs footer-title">Your Voice, My<br>Words.</h2>
<div class="abs brand site-footer-brand"><i class="brand-dot"></i>KLV Messaging</div>
<div class="abs subscribe-input">Enter your email</div>
<div class="abs btn-orange subscribe-btn">Subscribe</div>
<div class="abs foot-col col-company">
  <h3>Company</h3>
  <p>About</p><p>Contact</p><p>Services</p>
</div>
<div class="abs foot-col col-contact">
  <h3>Contact Info.</h3>
  <p>+972-50-618-2297</p><p>hello@klvmsg.co.il</p><p>P.O. Box 1208<br>Ramot Hadar, Israel 40700</p>
</div>
<i class="abs foot-rule"></i>
<p class="abs copyright">©Copyright 2023 KLV Messaging</p>

</body>
</html>
```